Design WORDPRESS Website for E Commerce Business

We are needing a WORDPRESS website for an E Commerce Business that is supplying quailty kids / baby products.

Target Market(s)

Female / Working Mums / New Mums

Industry/Entity Type

Business

Number of Pages Required

1 page

Font styles to use
Sans Serif

Colors
33b8a4
f8fcfd
d3a5cc
f7f1f7
cbcbcb
9d9d9d

```html
<!DOCTYPE html>
<html lang="en">
<head>
<meta charset="utf-8">
<title>Puddle &amp; Pip — Baby &amp; Kids Store</title>
<link rel="stylesheet" href="https://fonts.googleapis.com/css2?family=Arvo:ital,wght@0,400;0,700;1,400&family=Noto+Serif:wght@400;700&display=swap">
<style>
:root{
  --page-bg:#efe4d7;
  --panel:#ffffff;
  --panel-line:#ece6e0;
  --teal:#8fd6d8;
  --teal-deep:#6fc5c8;
  --teal-text:#7ccfd1;
  --ribbon:#a4e0e1;
  --ribbon-fold:#7fc9cc;
  --pink:#f9c1c7;
  --pink-deep:#f4a8b1;
  --heading:#5d5a58;
  --body:#6e6a68;
  --muted:#9d9d9d;
  --field-line:#dcdcdc;
}
*{box-sizing:border-box;margin:0;padding:0}
html,body{width:1200px;height:2778px;overflow:hidden}
body{background:var(--page-bg);font-family:"Noto Serif",serif;color:var(--body);position:relative}
.abs{position:absolute}
.frame{position:absolute;left:0;top:0}
.heading{font-family:"Arvo",serif;font-weight:700;color:var(--heading);letter-spacing:2px;text-align:center}
.heading-rule{display:block;width:118px;margin:12px auto 0;border-top:2px dotted #c9c4c0}

/* top badges */
.cart-badge{left:148px;top:37px;width:139px;height:139px;border-radius:50%;background:#fff;border:3px dotted #e8ded2;text-align:center;font-family:"Arvo",serif;font-size:14px;color:var(--body);padding-top:44px;line-height:34px}
.cart-badge svg{vertical-align:-3px;margin-right:6px}
.call-badge{left:917px;top:50px;width:179px;height:107px;background:#fff;border:3px dotted #e8ded2;border-radius:6px;text-align:center;font-family:"Arvo",serif}
.call-badge .label{color:var(--teal-text);font-size:21px;padding-top:18px;letter-spacing:1px}
.call-badge .number{color:var(--body);font-size:19px;margin-top:10px;letter-spacing:1px}

.brand{left:0;width:1200px;top:158px;display:flex;justify-content:center;align-items:center;gap:14px}
.brand-mark{width:58px;height:58px;border-radius:50%;background:#8a8685}
.brand-name{font-family:"Arvo",serif;font-weight:700;font-size:38px;color:var(--teal-deep);letter-spacing:1px}

/* nav */
.nav{left:130px;top:261px;width:935px;height:67px;display:flex;justify-content:center;align-items:center;gap:34px;font-family:"Arvo",serif;font-weight:700;font-size:17px;color:#fff;letter-spacing:1.5px}
.nav .active{background:#fff;color:var(--teal-deep);border-radius:14px;padding:3px 14px}

/* hero */
.hero{left:169px;top:326px;width:861px;height:511px;background:linear-gradient(110deg,#efe9e6 0%,#f6e6dc 40%,#d9b8a4 72%,#8c5a45 100%)}
.hero-arrow{width:34px;height:34px;border-radius:50%;background:rgba(120,120,120,.55);display:flex;align-items:center;justify-content:center}
.welcome{left:369px;top:432px;width:463px;height:215px;text-align:center}
.welcome .title{position:absolute;left:0;width:100%;top:92px;font-family:"Arvo",serif;font-weight:700;font-size:38px;color:var(--teal-deep);letter-spacing:3px}
.welcome .sub{position:absolute;left:0;width:100%;top:142px;font-family:"Arvo",serif;font-size:32px;color:#8b8684;letter-spacing:2px}

/* about */
.about{left:172px;top:898px;width:421px}
.about .heading{font-size:26px;width:372px}
.about p{font-size:13.5px;line-height:24px;letter-spacing:.6px;margin-top:22px}
.about p+p{margin-top:8px}
.btn{display:inline-block;background:var(--teal);color:#fff;font-family:"Arvo",serif;text-align:center;border-radius:3px}
.read-more{margin-top:30px;width:108px;height:26px;line-height:26px;font-size:13px}

.shop{left:694px;top:908px;width:347px;height:314px}
.shop-title{left:0;width:100%;top:50px;text-align:center;font-family:"Arvo",serif;font-weight:700;font-size:29px;color:#fff;letter-spacing:1px}
.shop-list{left:52px;top:104px;list-style:none;font-family:"Arvo",serif;font-weight:700;font-size:14px;color:#fff;letter-spacing:1.5px}
.shop-list li{height:33px;line-height:33px;display:flex;align-items:center;width:232px;padding-left:12px}
.shop-list li::before{content:"";width:12px;height:12px;border-radius:50%;background:#fff;margin-right:20px}
.shop-list li.current{background:#fff;color:var(--pink-deep);border-radius:12px;height:21px;line-height:21px;margin:6px 0}
.shop-list li.current::before{background:var(--pink)}

/* categories */
.category{width:256px;height:194px;border-radius:6px;border:2px solid #efebe8;overflow:hidden}
.category .photo{position:absolute;inset:0}
.category .tag{position:absolute;right:0;top:124px;width:176px;height:46px}
.category .tag span{position:absolute;right:0;width:130px;top:0;line-height:46px;text-align:center;font-family:"Arvo",serif;font-style:italic;font-weight:700;font-size:21px;color:#fff;letter-spacing:2px}

/* products */
.divider{left:169px;width:870px;border-top:2px dashed #d8d2cc}
.product{width:140px;text-align:center;top:1589px}
.product .art{width:110px;height:118px;margin:0 auto;border-radius:10px}
.product .name{font-family:"Arvo",serif;font-style:italic;font-size:17px;color:var(--body);margin-top:18px;letter-spacing:1px}
.product .price{font-family:"Arvo",serif;font-size:18px;color:var(--body);margin-top:2px}
.product .btn{width:108px;height:26px;line-height:26px;font-size:13px;margin-top:6px}
.slide-arrow{top:1682px}

/* partners */
.partners-heading{left:400px;width:400px;top:1864px;font-size:26px}
.partner{top:1972px;width:110px;height:92px}

/* footer */
.footer-col .heading{font-size:23px}
.contact-row{display:flex;align-items:center;gap:26px;font-size:16.5px;line-height:20px;letter-spacing:.5px}
.icon-circle{width:46px;height:46px;border-radius:50%;background:var(--teal);display:flex;align-items:center;justify-content:center;flex:none}
.social{display:flex;gap:23px}
.social span{width:46px;height:46px;border-radius:50%;background:var(--teal)}
.field{width:241px;height:33px;border:2px solid #e6e6e6;border-radius:3px;font-family:"Noto Serif",serif;font-style:italic;font-size:11px;color:var(--muted);padding:7px 10px;letter-spacing:.5px}
.field.message{height:108px}
.submit{width:124px;height:37px;line-height:37px;border-radius:18px;font-size:16px;font-weight:700;letter-spacing:1.5px}
.quick-links{list-style:none;font-family:"Arvo",serif;font-size:18px;color:var(--body);letter-spacing:1.5px;line-height:30px}
.copyright{left:0;width:1200px;top:2698px;text-align:center;font-family:"Arvo",serif;font-weight:700;font-size:17px;color:#7a7675;letter-spacing:1.5px}
.copyright b{color:var(--teal-text)}
</style>
</head>
<body>

<!-- hanging strings -->
<svg class="frame" width="1200" height="2778" aria-hidden="true">
  <line x1="217" y1="0" x2="217" y2="40" stroke="#fff" stroke-width="3" stroke-dasharray="6 5"/>
  <line x1="922" y1="0" x2="922" y2="52" stroke="#fff" stroke-width="3" stroke-dasharray="6 5"/>
  <line x1="1090" y1="0" x2="1090" y2="52" stroke="#fff" stroke-width="3" stroke-dasharray="6 5"/>
  <!-- main house panel -->
  <path d="M93,255 Q93,185 163,185 L287,185 L600,70 L913,185 L1037,185 Q1107,185 1107,255 L1107,2078 Q1107,2148 1037,2148 L163,2148 Q93,2148 93,2078 Z" fill="#fff"/>
  <path d="M107,262 Q107,199 170,199 L290,199 L600,85 L910,199 L1030,199 Q1093,199 1093,262 L1093,2071 Q1093,2134 1030,2134 L170,2134 Q107,2134 107,2071 Z" fill="none" stroke="#eeeae6" stroke-width="2"/>
  <!-- footer panel -->
  <rect x="93" y="2170" width="1014" height="482" rx="60" fill="#fff"/>
  <rect x="107" y="2184" width="986" height="454" rx="50" fill="none" stroke="#eeeae6" stroke-width="2"/>
  <!-- copyright bar -->
  <rect x="93" y="2674" width="1014" height="74" rx="37" fill="#fff"/>
  <rect x="104" y="2684" width="992" height="54" rx="27" fill="none" stroke="#eeeae6" stroke-width="2"/>
  <!-- nav ribbon tails -->
  <polygon points="33,288 150,288 150,354 33,354 66,321" fill="var(--ribbon)"/>
  <polygon points="1167,288 1050,288 1050,354 1167,354 1134,321" fill="var(--ribbon)"/>
  <polygon points="130,328 150,354 150,328" fill="var(--ribbon-fold)"/>
  <polygon points="1070,328 1050,354 1050,328" fill="var(--ribbon-fold)"/>
  <rect x="130" y="261" width="940" height="67" fill="var(--ribbon)"/>
  <line x1="130" y1="266" x2="1070" y2="266" stroke="#c6ecec" stroke-width="2"/>
</svg>

<div class="abs cart-badge">
  <div><svg width="16" height="16" viewBox="0 0 16 16"><path d="M3 5h10l-1 9H4z" fill="none" stroke="#7ccfd1" stroke-width="1.5"/><path d="M6 5V3.5a2 2 0 0 1 4 0V5" fill="none" stroke="#7ccfd1" stroke-width="1.5"/></svg>0 items</div>
  <div>$0.00</div>
</div>
<div class="abs call-badge">
  <div class="label">Call Us</div>
  <div class="number">555-210-4476</div>
</div>

<div class="abs brand">
  <span class="brand-mark"></span>
  <span class="brand-name">Puddle &amp; Pip</span>
</div>

<nav class="abs nav">
  <span>Home</span><span>Pages</span><span>Shop</span><span>Gallery</span><span class="active">Blog</span><span>Contact</span>
</nav>

<div class="abs hero" role="img" aria-label="Photo of a mother resting beside her smiling baby on soft white bedding"></div>
<div class="abs hero-arrow" style="left:181px;top:552px"><svg width="12" height="14"><path d="M9 2 3 7l6 5" stroke="#fff" stroke-width="2.5" fill="none"/></svg></div>
<div class="abs hero-arrow" style="left:978px;top:549px"><svg width="12" height="14"><path d="M3 2l6 5-6 5" stroke="#fff" stroke-width="2.5" fill="none"/></svg></div>
<div class="abs welcome">
  <svg class="frame" width="463" height="215" aria-hidden="true">
    <path d="M60,70 L140,70 A92,70 0 0 1 323,70 L403,70 A50,50 0 0 1 403,170 L380,170 A150,45 0 0 1 83,170 L60,170 A50,50 0 0 1 60,70 Z" fill="rgba(255,255,255,.72)" stroke="#9edadb" stroke-width="3"/>
  </svg>
  <div class="title">WELCOME TO</div>
  <div class="sub">Puddle&amp;Pip</div>
</div>

<section class="abs about">
  <h2 class="heading">About Us<span class="heading-rule"></span></h2>
  <p>Lorem ipsum dolor sit amet, consectetur adipiscing elit. Vestibulum et molestie nisl. Maecenas non tortor eget tortor imperdiet consectetur nec vitae eros. Integer a est nibh. Nunc fermentum porta mi. Nam sed fermentum mi. Nulla vel rhoncus sem. Suspendisse in eros et dui ultrices commodo.</p>
  <p>Lorem ipsum dolor sit amet, consectetur adipiscing elit. Vestibulum et molestie nisl.</p>
  <span class="btn read-more">Read more</span>
</section>

<aside class="abs shop">
  <svg class="frame" width="347" height="314" aria-hidden="true">
    <path d="M6,32 Q6,18 20,18 L100,18 Q140,2 173,2 Q206,2 246,18 L327,18 Q341,18 341,32 L341,296 Q341,310 327,310 L20,310 Q6,310 6,296 Z" fill="none" stroke="var(--pink)" stroke-width="2.5" stroke-dasharray="3 4"/>
    <path d="M14,40 Q14,26 28,26 L104,26 Q140,10 173,10 Q206,10 242,26 L319,26 Q333,26 333,40 L333,288 Q333,302 319,302 L28,302 Q14,302 14,288 Z" fill="var(--pink)"/>
    <path d="M28,56 Q28,44 40,44 L112,44 Q142,30 173,30 Q204,30 234,44 L307,44 Q319,44 319,56 L319,276 Q319,288 307,288 L40,288 Q28,288 28,276 Z" fill="none" stroke="#fff" stroke-width="2.5"/>
  </svg>
  <div class="abs shop-title">Shop</div>
  <ul class="abs shop-list">
    <li>ALL PRODUCTS</li>
    <li class="current">BOYS</li>
    <li>GIRLS</li>
    <li>ACCESSORIES</li>
    <li>SALES AND DISCOUNTS</li>
  </ul>
</aside>

<!-- category cards -->
<div class="abs category" style="left:196px;top:1278px">
  <div class="photo" role="img" aria-label="Photo of a baby girl with a pink headband in a basket" style="background:linear-gradient(160deg,#f7f3f1,#f1dcd6 60%,#e9c3c2)"></div>
  <div class="tag"><svg width="176" height="46"><polygon points="0,0 176,0 176,46 0,46 22,23" fill="var(--pink)"/><polygon points="28,0 46,23 28,46 40,46 58,23 40,0" fill="#fbd6da"/></svg><span>Girls</span></div>
</div>
<div class="abs category" style="left:472px;top:1278px">
  <div class="photo" role="img" aria-label="Photo of a laughing baby boy in yellow among soft blue toys" style="background:linear-gradient(160deg,#eef3f6,#cfe0ea 55%,#e7d9b8)"></div>
  <div class="tag"><svg width="176" height="46"><polygon points="0,0 176,0 176,46 0,46 22,23" fill="var(--pink)"/><polygon points="28,0 46,23 28,46 40,46 58,23 40,0" fill="#fbd6da"/></svg><span>Boys</span></div>
</div>
<div class="abs category" style="left:748px;top:1278px">
  <div class="photo" role="img" aria-label="Photo of folded baby clothes stacked with a plush toy on top" style="background:linear-gradient(160deg,#f6f8f9,#cbe9ec 55%,#a9d8d6)"></div>
  <div class="tag"><svg width="176" height="46"><polygon points="0,0 176,0 176,46 0,46 22,23" fill="var(--pink)"/><polygon points="28,0 46,23 28,46 40,46 58,23 40,0" fill="#fbd6da"/></svg><span>Sales</span></div>
</div>

<!-- products -->
<div class="abs divider" style="top:1567px"></div>
<svg class="abs slide-arrow" style="left:142px" width="20" height="30" aria-hidden="true"><path d="M17 2 3 15l14 13" stroke="#cbcbcb" stroke-width="2.5" fill="none"/></svg>
<svg class="abs slide-arrow" style="left:1038px" width="20" height="30" aria-hidden="true"><path d="M3 2l14 13L3 28" stroke="#cbcbcb" stroke-width="2.5" fill="none"/></svg>

<div class="abs product" style="left:184px"><div class="art" role="img" aria-label="Pink girl overalls with a cupcake patch" style="background:linear-gradient(#f6c4da,#e9a9c7)"></div><div class="name">Girl overalls</div><div class="price">$20</div><span class="btn">Add to Cart</span></div>
<div class="abs product" style="left:356px"><div class="art" role="img" aria-label="Sage green shorts" style="background:linear-gradient(#8fbfae,#6fa594)"></div><div class="name">Girl overalls</div><div class="price">$40</div><span class="btn">Add to Cart</span></div>
<div class="abs product" style="left:534px"><div class="art" role="img" aria-label="Pink and white striped romper" style="background:linear-gradient(#f8d3d6,#f0a5ad)"></div><div class="name">Girl overalls</div><div class="price">$70</div><span class="btn">Add to Cart</span></div>
<div class="abs product" style="left:721px"><div class="art" role="img" aria-label="White smock top with denim shorts" style="background:linear-gradient(#f7f6f4,#b9c7da)"></div><div class="name">Girl overalls</div><div class="price">$30</div><span class="btn">Add to Cart</span></div>
<div class="abs product" style="left:886px"><div class="art" role="img" aria-label="Pink floral baby romper" style="background:linear-gradient(#fbe7ea,#f3c6cd)"></div><div class="name">Girl overalls</div><div class="price">$13</div><span class="btn">Add to Cart</span></div>

<div class="abs divider" style="top:1820px"></div>

<!-- partners -->
<h2 class="abs heading partners-heading">Our Partners<span class="heading-rule"></span></h2>
<svg class="abs partner" style="left:195px" role="img" aria-label="Partner badge"><circle cx="55" cy="46" r="36" fill="#f6c9d2"/></svg>
<svg class="abs partner" style="left:367px" role="img" aria-label="Partner badge"><ellipse cx="55" cy="46" rx="52" ry="36" fill="none" stroke="#7b5a47" stroke-width="4"/></svg>
<svg class="abs partner" style="left:541px" role="img" aria-label="Partner badge"><rect x="16" y="10" width="78" height="72" rx="14" fill="#c9e3f1"/></svg>
<svg class="abs partner" style="left:708px" role="img" aria-label="Partner badge"><ellipse cx="55" cy="46" rx="54" ry="30" fill="#e7c0b8"/></svg>
<svg class="abs partner" style="left:888px" role="img" aria-label="Partner badge"><ellipse cx="55" cy="46" rx="54" ry="40" fill="none" stroke="#5f8f99" stroke-width="4"/></svg>

<!-- footer -->
<section class="abs footer-col" style="left:160px;top:2220px;width:300px">
  <h3 class="heading" style="width:240px;margin-left:0">Contact Us</h3>
  <div class="contact-row" style="margin-top:48px"><span class="icon-circle"><svg width="22" height="22" viewBox="0 0 24 24"><path d="M6.6 10.8a15 15 0 0 0 6.6 6.6l2.2-2.2a1 1 0 0 1 1-.25 11.4 11.4 0 0 0 3.6.6 1 1 0 0 1 1 1V20a1 1 0 0 1-1 1A17 17 0 0 1 3 4a1 1 0 0 1 1-1h3.5a1 1 0 0 1 1 1c0 1.25.2 2.45.6 3.6a1 1 0 0 1-.25 1z" fill="#fff"/></svg></span><span>555-210-4476<br>555-318-6620</span></div>
  <div class="contact-row" style="margin-top:30px"><span class="icon-circle"><svg width="20" height="24" viewBox="0 0 20 24"><path d="M10 1a8 8 0 0 0-8 8c0 6 8 14 8 14s8-8 8-14a8 8 0 0 0-8-8zm0 11a3 3 0 1 1 0-6 3 3 0 0 1 0 6z" fill="#fff"/></svg></span><span>27 Willow Lane,<br>Fernbrook 204518</span></div>
  <div class="contact-row" style="margin-top:24px"><span class="icon-circle"><svg width="22" height="16" viewBox="0 0 22 16"><rect x="1" y="1" width="20" height="14" rx="2" fill="#fff"/><path d="M2 2l9 7 9-7" stroke="#8fd6d8" stroke-width="1.8" fill="none"/></svg></span><span>hello@puddlepip.mail</span></div>
  <div class="social" style="margin-top:34px"><span></span><span></span><span></span><span></span></div>
</section>

<section class="abs footer-col" style="left:524px;top:2220px;width:241px">
  <h3 class="heading">Email Us</h3>
  <div class="field" style="margin-top:36px">Name...</div>
  <div class="field" style="margin-top:20px">Email...</div>
  <div class="field message" style="margin-top:18px">Message...</div>
  <span class="btn submit" style="margin:18px 0 0 58px">Submit</span>
</section>

<section class="abs footer-col" style="left:862px;top:2220px;width:160px">
  <h3 class="heading" style="text-align:left">Quick Links</h3>
  <ul class="quick-links" style="margin-top:34px">
    <li>Home</li><li>Pages</li><li>Shop</li><li>Testimonials</li><li>Gallery</li><li>Blog</li><li>Contact</li>
  </ul>
</section>

<div class="abs copyright">© 2017Copyright - <b>Puddle&amp;Pip</b></div>

</body>
</html>
```